mediation practice website build

Looking to create a website for new civil mediation practice. Pages would be "home", "about us", "about mediation", "scheduling" (perhaps with some kind of calendar function), "contact us". Would love to be able to update content/text myself.
Reason: Still working on revisions with the designs submitted. Thanks to all for your submissions!
Small to midsize businesses and attorneys representing those size businesses in pending disputes.
Build

```html
<!DOCTYPE html>
<html lang="en">
<head>
<meta charset="utf-8">
<title>Oakline Mediation</title>
<link href="https://fonts.googleapis.com/css2?family=Arimo:ital,wght@0,400;0,700;1,400&family=Open+Sans:wght@400&display=swap" rel="stylesheet">
<style>
:root{
  --navy:#0b4780;
  --heading:#174f86;
  --band:#2c6094;
  --green:#1f4d1f;
  --footer:#063f78;
  --link:#2a8ad8;
  --text:#222;
  --rule:#c8c8c8;
}
*{margin:0;padding:0;box-sizing:border-box}
html,body{width:1200px;height:641px;overflow:hidden;background:#fff;font-family:"Arimo",Arial,sans-serif;color:var(--text)}
.page{position:relative;width:1200px;height:641px}
.top-line{position:absolute;left:0;top:30px;width:1200px;height:5px;background:var(--green)}
.nav-band{position:absolute;left:0;top:35px;width:1200px;height:53px;background:var(--band)}
.brand{position:absolute;left:126px;top:15px;width:251px;height:73px;background:#fff;display:flex;align-items:center;gap:10px;padding-left:12px}
.brand-mark{width:14px;height:14px;background:var(--heading);flex:none}
.brand-name{color:var(--heading);font-weight:700;font-size:21px;line-height:24px}
.main-nav{position:absolute;left:393px;top:52px;display:flex;gap:41px}
.main-nav a{color:#fff;text-decoration:none;font-weight:700;font-size:18px;letter-spacing:.8px}
.content{position:absolute;left:126px;top:88px;width:963px;height:467px;border-left:2px solid var(--rule);border-right:2px solid var(--rule)}
.col-left{position:absolute;left:15px;top:44px;width:600px}
h2{color:var(--heading);font-size:20px;line-height:22px;font-weight:700;padding-bottom:6px;border-bottom:2px solid var(--heading)}
.intro{font-size:12.4px;font-weight:700;letter-spacing:.8px;line-height:15px;text-align:justify;margin-top:22px;color:#111}
.more{display:block;text-align:right;color:var(--link);font-size:12.4px;line-height:15px;font-weight:700;letter-spacing:1px;text-decoration:none;margin-top:4px;margin-bottom:1px}
.contact{margin-top:20px;border-top:3px solid var(--heading);padding-top:7px;font-size:14.5px;line-height:16px}
.contact .lead{font-weight:700;color:#111}
.contact .person{font-weight:700;font-size:16.5px;line-height:18px;margin:9px 0 4px}
.contact p{margin-bottom:16px}
.col-right{position:absolute;left:647px;top:44px;width:290px}
.month{text-align:center;font-weight:700;font-size:17.5px;line-height:20px;color:var(--heading);margin:22px 0 8px}
.calendar{margin-left:2px;width:286px;background:var(--navy);display:grid;grid-template-columns:repeat(7,1fr);gap:2px;padding:0 2px 2px}
.calendar .dow{height:26px;display:flex;align-items:center;justify-content:center;color:#fff;font-weight:700;font-size:14px}
.calendar .day{height:30px;background:#fff;display:flex;align-items:center;justify-content:center;color:var(--navy);font-weight:700;font-size:14px}
.calendar .blank{grid-column:span 2;height:30px;background:#fff}
.calendar .today{background:var(--navy);color:#fff;outline:2px solid #fff;outline-offset:-4px}
.cal-nav{grid-column:span 7;display:flex;justify-content:space-between;color:#fff;font-weight:700;font-size:14px;padding:4px 2px 3px}
.bottom-line{position:absolute;left:0;top:555px;width:1200px;height:5px;background:var(--green)}
.footer{position:absolute;left:0;top:560px;width:1200px;height:81px;background:var(--footer);color:#fff;font-family:"Open Sans",Verdana,sans-serif;font-size:10px;text-align:center}
.footer-nav{margin-top:26px;margin-left:15px}
.footer-nav a{color:#fff;text-decoration:none;padding:0 7px}
.copyright{margin-top:7px;margin-left:8px}
</style>
</head>
<body>
<div class="page">
  <div class="top-line"></div>
  <div class="nav-band"></div>
  <div class="brand"><span class="brand-mark"></span><span class="brand-name">Oakline Mediation</span></div>
  <nav class="main-nav">
    <a href="#">Home</a><a href="#">About Us</a><a href="#">About Mediation</a><a href="#">Scheduling</a><a href="#">Contact Us</a>
  </nav>

  <main class="content">
    <section class="col-left">
      <h2>What is Civil Mediation?</h2>
      <p class="intro">Lorem ipsum dolor sit amet, sectetu adip scing varius interdum incid unt quis, libero. Aenean mturpis. Maecenas hendrerit masa laoreet iaculipede mnisl ulamcorper.</p>
      <a class="more" href="#">read more</a>
      <h2>Why Choose Oakline Mediation?</h2>
      <p class="intro">Lorem ipsum dolor sit amet, sectetu adip scing varius interdum incid unt quis, libero. Aenean mturpis. Maecenas hendrerit masa laoreet iaculipede mnisl ulamcorper.</p>
      <a class="more" href="#">read more</a>
      <div class="contact">
        <div class="lead">To set up an appointment, please contact Name Name at:</div>
        <div class="person">Name Name</div>
        <p><em>Title</em><br>Adress Line 1<br>Adress Line 2<br>City, State and PIN</p>
        <div><strong>Phone:</strong> +1-555-204-1180<br><strong>Fax:</strong> +1-555-204-1191<br><strong>Email:</strong> info@oaklinemediation.com</div>
      </div>
    </section>

    <aside class="col-right">
      <h2>Scheduling</h2>
      <div class="month">June 2011</div>
      <div class="calendar">
        <div class="dow">M</div><div class="dow">T</div><div class="dow">W</div><div class="dow">T</div><div class="dow">F</div><div class="dow">S</div><div class="dow">S</div>
        <div class="blank"></div><div class="day">1</div><div class="day">2</div><div class="day">3</div><div class="day">4</div><div class="day">5</div>
        <div class="day today">6</div><div class="day">7</div><div class="day">8</div><div class="day">9</div><div class="day">10</div><div class="day">11</div><div class="day">12</div>
        <div class="day">13</div><div class="day">14</div><div class="day">15</div><div class="day">16</div><div class="day">17</div><div class="day">18</div><div class="day">19</div>
        <div class="day">20</div><div class="day">21</div><div class="day">22</div><div class="day">23</div><div class="day">24</div><div class="day">25</div><div class="day">26</div>
        <div class="day">27</div><div class="day">28</div><div class="day">29</div><div class="day">30</div><div class="day">31</div><div class="blank"></div>
        <div class="cal-nav"><span>« May</span><span>Jul »</span></div>
      </div>
    </aside>
  </main>

  <div class="bottom-line"></div>
  <footer class="footer">
    <div class="footer-nav"><a href="#">HOME</a><span>|</span><a href="#">ABOUT US</a><span>|</span><a href="#">ABOUT MEDIATION</a><span>|</span><a href="#">SCHEDULING</a><span>|</span><a href="#">CONTACT US</a></div>
    <div class="copyright">Copyright © Oakline Mediation.</div>
  </footer>
</div>
</body>
</html>
```